High end business card design for custom homebuilding company

Looking for a high end business card design that is unique and elegant. Can use embossing, foil printing, laser die cutting, or any high end printing technique or high end paper. Will upload current design so you can see the logo and what we are using currently, but we want something more unique and elegant. I included our logo to help with design.

Target Market(s)

High end custom home buyers of $1.5 million plus homes. Also real estate developers of high end communities.

Industry/Entity Type

Business

Contact Information for Business Card

Double sided. We want something very elegant and expensive looking. We are looking to incorporate a combination of perhaps linen paper or a high end paper, with foil stamping or embossing/debossing to make the card look unique, but still elegant. We tend to use blacks and golds, but are open to any ideas. Looking for creative and unique design.

Colors

Designer to choose colors to be used in the design.

Requirements
Must have
• High end, elegant look. Can use foil, embossing, or high end papers like linen. We want to make the card unique and interesting, but elegant and expensive looking.
Nice to have
• I am including just some cards I saw that looked interesting for one reason or another. I like a clean elegant design and like both the clean white style, and the blacks. So not sure if we want a black design or white. Would like to see both.

```html
<!DOCTYPE html>
<html lang="en">
<head>
<meta charset="utf-8">
<title>Kestrel Ridge Custom Homes – Business Card</title>
<link href="https://fonts.googleapis.com/css2?family=Noto+Serif:wght@400;700&display=swap" rel="stylesheet">
<style>
  :root {
    --backdrop: #e0e0dd;
    --card-dark: #1f2624;
    --card-light: #efefec;
    --gold: #d2a052;
    --copper: #9b6552;
  }
  * { margin: 0; padding: 0; box-sizing: border-box; }
  html, body { width: 1200px; height: 1000px; overflow: hidden; }
  body {
    background: var(--backdrop);
    font-family: "Noto Serif", Georgia, serif;
    position: relative;
  }
  .card {
    position: absolute;
    width: 581px;
    height: 323px;
    box-shadow: 0 2px 4px rgba(0,0,0,0.25);
  }
  .card--front {
    left: 338px; top: 158px;
    background: var(--card-dark);
    color: var(--gold);
  }
  .card--back {
    left: 335px; top: 510px;
    background: var(--card-light);
    color: var(--copper);
    text-align: center;
  }
  .brand {
    position: absolute;
    left: 47px; top: 118px;
    display: flex;
    align-items: center;
    gap: 12px;
  }
  .brand__mark {
    width: 44px; height: 44px;
    border-radius: 50%;
    border: 2px solid var(--gold);
  }
  .brand__name {
    font-weight: 700;
    font-size: 29px;
    line-height: 1;
    letter-spacing: 1px;
    text-transform: uppercase;
  }
  .brand__tagline {
    font-weight: 700;
    font-size: 11px;
    letter-spacing: 10px;
    text-transform: uppercase;
    margin-top: 4px;
  }
  .social {
    position: absolute;
    right: 41px; top: 238px;
    text-align: right;
  }
  .social__label {
    font-size: 7px;
    letter-spacing: 1.5px;
    margin-bottom: 6px;
  }
  .social__icons { display: flex; gap: 3px; justify-content: flex-end; }
  .social__icon {
    width: 16px; height: 16px;
    border-radius: 50%;
    background: var(--gold);
  }
  .website {
    position: absolute;
    right: 41px; top: 283px;
    font-size: 7px;
    letter-spacing: 1.6px;
  }
  .contact { padding-top: 59px; }
  .contact__name {
    font-weight: 700;
    font-size: 16px;
    line-height: 20px;
    letter-spacing: 3.5px;
    text-transform: uppercase;
    margin-bottom: 28px;
  }
  .contact__item {
    font-weight: 700;
    font-size: 13px;
    letter-spacing: 1.2px;
    line-height: 20px;
  }
  .contact__icon {
    display: block;
    margin: 0 auto 6px;
    width: 14px; height: 14px;
    fill: var(--copper);
  }
  .contact__item + .contact__icon { margin-top: 8px; }
</style>
</head>
<body>
  <section class="card card--front">
    <div class="brand">
      <div class="brand__mark"></div>
      <div>
        <div class="brand__name">Kestrel Ridge</div>
        <div class="brand__tagline">Custom Homes</div>
      </div>
    </div>
    <div class="social">
      <div class="social__label">follow us on:</div>
      <div class="social__icons">
        <span class="social__icon"></span>
        <span class="social__icon"></span>
        <span class="social__icon"></span>
        <span class="social__icon"></span>
        <span class="social__icon"></span>
      </div>
    </div>
    <div class="website">www.kestrelridgehomes.com.au</div>
  </section>

  <section class="card card--back">
    <div class="contact">
      <div class="contact__name">Dummy Name</div>
      <svg class="contact__icon" viewBox="0 0 24 24" aria-hidden="true"><path d="M6.6 10.8a15.1 15.1 0 0 0 6.6 6.6l2.2-2.2a1 1 0 0 1 1-.25 11.4 11.4 0 0 0 3.6.57 1 1 0 0 1 1 1V20a1 1 0 0 1-1 1A17 17 0 0 1 3 4a1 1 0 0 1 1-1h3.5a1 1 0 0 1 1 1c0 1.25.2 2.45.57 3.57a1 1 0 0 1-.25 1z"/></svg>
      <div class="contact__item">Dummy Phone</div>
      <svg class="contact__icon" viewBox="0 0 24 24" aria-hidden="true"><path d="M2 5h20v14H2z"/><path d="M2 6l10 7.5L22 6" fill="none" stroke="var(--card-light)" stroke-width="1.5"/></svg>
      <div class="contact__item">Dummy@krhomes.com.au</div>
      <svg class="contact__icon" viewBox="0 0 24 24" aria-hidden="true"><path d="M12 2a7 7 0 0 0-7 7c0 5.2 7 13 7 13s7-7.8 7-13a7 7 0 0 0-7-7zm0 9.5A2.5 2.5 0 1 1 12 6.5a2.5 2.5 0 0 1 0 5z"/></svg>
      <div class="contact__item">Unit 3 14-18 Halden Road,<br>Belmore, WA 6110</div>
    </div>
  </section>
</body>
</html>
```